Software as a Service to manage Home Care Management

We need a web site designed for Home Care Management Software as a Service product, that facilitates Home Care organizations to manage and schedule carers to visit client homes. We want a modern look and feel using our existing logo.

Target Market(s)

Home Care Management organizations. Product is similar to: https://kelvantro.co/

Coding

Coded - Design and coding required

Number of Pages Required

3 page

```html
<!DOCTYPE html>
<html lang="en">
<head>
<meta charset="utf-8">
<title>Tendwell – Home Care Management</title>
<link rel="stylesheet" href="https://fonts.googleapis.com/css2?family=Fira+Sans:wght@400;500;600;700&display=swap">
<style>
:root{
  --pink:#ef4379;
  --pink-deep:#d7336a;
  --ink:#333438;
  --muted:#6b6b70;
  --grey-band:#dcdcdc;
  --grey-light:#ececec;
  --dark:#2f2f31;
  --slate:#3b3f52;
  --footer:#cdc6c6;
  --white:#ffffff;
}
*{box-sizing:border-box;margin:0;padding:0}
html,body{width:1200px;height:1200px;overflow:hidden;background:var(--white)}
body{font-family:"Fira Sans",sans-serif;color:var(--ink)}
.stage{position:absolute;left:3px;top:0;width:1920px;height:1930px;transform:scale(0.6218);transform-origin:0 0}
.page{position:absolute;left:743px;top:0;width:446px;height:1930px;background:var(--white)}
.abs{position:absolute}
.center{left:0;right:0;text-align:center}

/* nav */
.brand{left:32px;top:6px;display:flex;align-items:center;gap:4px}
.brand-dot{width:14px;height:14px;border-radius:50%;background:var(--pink)}
.brand-name{font-size:10px;font-weight:500;color:var(--ink);letter-spacing:.3px}
.nav{left:190px;top:12px;display:flex;gap:12px;font-size:5px;letter-spacing:.8px;font-weight:500}
.nav .active{border-bottom:1px solid var(--pink);padding-bottom:2px}
.btn{background:var(--pink);color:var(--white);border-radius:9px;font-size:4.5px;font-weight:600;letter-spacing:.8px;display:flex;align-items:center;justify-content:center;text-transform:uppercase}

/* hero */
.hero{top:31px;left:0;width:446px;height:266px;background:linear-gradient(100deg,#ee7aab 0%,#c0569b 45%,#8d4a9c 100%)}
.hero-title{top:104px;font-size:21px;font-weight:600;color:var(--white);line-height:21px}
.hero-sub{top:152px;font-size:9px;color:#f4e4ef;line-height:13px}

/* software band */
.software{top:297px;left:0;width:446px;height:293px;background:linear-gradient(160deg,#e6e6e6,#d6d6d6);clip-path:polygon(0 0,100% 0,100% 228px,0 100%)}
.h2{font-size:20.5px;font-weight:600;line-height:21px;color:var(--ink)}
.sub{font-size:9px;color:var(--muted);line-height:11px}
.para{font-size:5.6px;line-height:9px;color:var(--muted)}

/* benefits */
.benefits{left:30px;top:677px;width:210px;list-style:none}
.benefits li{display:flex;gap:10px;font-size:5.5px;line-height:9px;color:var(--muted);margin-bottom:9px}
.benefits b{color:var(--ink);font-weight:600}
.tick{flex:none;width:10px;height:10px;margin-top:1px}

/* testimonials */
.quotes{top:869px;left:0;width:446px;height:196px;background:linear-gradient(150deg,#e0e0e0,#d2d2d2)}
.quote{width:156px}
.quote-mark{color:var(--pink);font-size:16px;font-weight:700;line-height:10px}
.quote-text{font-size:8.6px;line-height:15.6px;color:var(--muted)}
.quote-rule{height:1px;background:#a9a9ad}
.quote-name{font-size:4.6px;letter-spacing:.8px;color:var(--muted);font-weight:600}
.quote-role{font-size:4.6px;color:#8c8c92}
.chev{font-size:12px;color:#777;font-weight:400}

/* demo */
.demo{top:1065px;left:0;width:446px;height:260px;background:linear-gradient(160deg,#3e4257 0%,#4a4d5c 50%,#6d6a6a 100%)}

/* team */
.member{width:116px;text-align:center}
.member.card{background:var(--white);box-shadow:0 0 6px rgba(0,0,0,.18)}
.avatar{display:block;width:56px;height:56px;border-radius:50%;margin:0 auto;background:linear-gradient(160deg,#8a8079,#3d3532)}
.m-text{font-size:5.8px;line-height:6.5px;color:var(--muted);margin-top:11px}
.m-name{font-size:4.6px;letter-spacing:.8px;font-weight:600;margin-top:8px}
.m-role{font-size:4.6px;color:#8c8c92;line-height:6px}

/* join */
.join{top:1675px;left:0;width:446px;height:200px;background:linear-gradient(160deg,#2a2a2b,#3a3a3c);clip-path:polygon(0 0,100% 33px,100% 100%,0 100%)}
.email{left:115px;top:1820px;width:149px;height:15px;background:#4a4a4c;border:1px solid #5d5d60;font-size:5px;color:var(--white);padding:4px 6px}

.footer{top:1875px;left:0;width:446px;height:55px;background:var(--footer);font-size:5.6px;color:var(--ink);line-height:7px}
</style>
</head>
<body>
<div class="stage">
<div class="page">

  <!-- navigation -->
  <div class="abs brand"><span class="brand-dot"></span><span class="brand-name">TENDWELL</span></div>
  <nav class="abs nav"><span>HOME</span><span class="active">ABOUT US</span><span>PRICING</span><span>CONTACT</span></nav>
  <div class="abs btn" style="left:345px;top:7px;width:69px;height:17px">Book a demo</div>

  <!-- hero -->
  <section class="abs hero" role="img" aria-label="Photo of a smiling caregiver with an elderly woman in a wheelchair, tinted pink to purple"></section>
  <h1 class="abs center hero-title">Delivering More<br>Time To Care</h1>
  <p class="abs center hero-sub">Provides greater peace of mind for your<br>clients and their families</p>

  <!-- software -->
  <section class="abs software"></section>
  <h2 class="abs center h2" style="top:337px">The Ultimate Care<br>Management Software</h2>
  <p class="abs center sub" style="top:383px">Built specifically for home care agencies</p>
  <svg class="abs" style="left:64px;top:417px" width="168" height="100" viewBox="0 0 168 100">
    <rect x="16" y="1" width="134" height="93" rx="3" fill="#fff" stroke="#d4d4d4"/>
    <rect x="0" y="93" width="166" height="4" rx="2" fill="#e9e9e9"/>
    <g fill="#9ed92e">
      <rect x="34" y="62" width="2" height="20"/><rect x="42" y="66" width="2" height="16"/><rect x="52" y="48" width="2" height="34"/>
      <rect x="60" y="74" width="2" height="8"/><rect x="70" y="68" width="2" height="14"/><rect x="80" y="64" width="2" height="18"/>
      <rect x="90" y="54" width="2" height="28"/><rect x="100" y="70" width="2" height="12"/><rect x="110" y="60" width="2" height="22"/>
      <rect x="120" y="66" width="2" height="16"/><rect x="130" y="58" width="2" height="24"/>
    </g>
    <g fill="#2cb8c6">
      <rect x="37" y="70" width="2" height="12"/><rect x="56" y="66" width="2" height="16"/><rect x="74" y="72" width="2" height="10"/>
      <rect x="84" y="70" width="2" height="12"/><rect x="104" y="68" width="2" height="14"/><rect x="124" y="70" width="2" height="12"/>
    </g>
    <polyline points="34,76 52,72 70,58 90,52 110,60 130,46 142,44" fill="none" stroke="#f2c94c" stroke-width="1"/>
    <g fill="#cfd3d8"><rect x="22" y="9" width="8" height="2"/><rect x="24" y="19" width="14" height="2"/><rect x="42" y="19" width="14" height="2"/><rect x="60" y="19" width="14" height="2"/><rect x="118" y="19" width="16" height="2"/></g>
  </svg>
  <p class="abs para" style="left:246px;top:428px;width:170px">Minim veniam, quis nostrud exercitation ullamco laboris nisi ut aliquip ex ea commodo consequat. Duis aute irure dolor in reprehenderit in voluptate velit esse cillum dolore eu fugiat nulla pariatur. Excepteur sint occaecat cupidatat non proident, sunt in culpa qui officia deserunt mollit anim id est laborum.</p>
  <div class="abs btn" style="left:293px;top:510px;width:60px;height:15px">Read more</div>

  <!-- benefits -->
  <h2 class="abs center h2" style="top:612px">Benefits of Our Software</h2>
  <p class="abs center sub" style="top:635px">Lorem ipsum dolor sit amet, consectetur adipiscing elit</p>
  <ul class="abs benefits">
    <li><svg class="tick" viewBox="0 0 10 10"><circle cx="5" cy="5" r="5" fill="var(--pink)"/><path d="M2.8 5.2l1.5 1.5 3-3" stroke="#fff" stroke-width="1.2" fill="none"/></svg><span><b>Effectively manage workflow</b> even in the midst of the COVID-19 pandemic, while having to maintain social distancing by staying remote and virtual</span></li>
    <li><svg class="tick" viewBox="0 0 10 10"><circle cx="5" cy="5" r="5" fill="var(--pink)"/><path d="M2.8 5.2l1.5 1.5 3-3" stroke="#fff" stroke-width="1.2" fill="none"/></svg><span><b>Eliminate paper.</b> No need for caregivers to drop off documents.</span></li>
    <li><svg class="tick" viewBox="0 0 10 10"><circle cx="5" cy="5" r="5" fill="var(--pink)"/><path d="M2.8 5.2l1.5 1.5 3-3" stroke="#fff" stroke-width="1.2" fill="none"/></svg><span><b>Live monitor visit activities</b> – know which caregiver has started the visit and who is delayed</span></li>
    <li><svg class="tick" viewBox="0 0 10 10"><circle cx="5" cy="5" r="5" fill="var(--pink)"/><path d="M2.8 5.2l1.5 1.5 3-3" stroke="#fff" stroke-width="1.2" fill="none"/></svg><span><b>Process all payers</b> – Medicaid/waiver in any state, managed care, Medicare, private insurance, long term care, VA and private pay</span></li>
    <li><svg class="tick" viewBox="0 0 10 10"><circle cx="5" cy="5" r="5" fill="var(--pink)"/><path d="M2.8 5.2l1.5 1.5 3-3" stroke="#fff" stroke-width="1.2" fill="none"/></svg><span>Use the software from <b>any device</b> – smartphones, tablets, laptops or desktops</span></li>
  </ul>
  <div class="abs" style="left:265px;top:660px;width:181px;height:155px;background:linear-gradient(150deg,#f1f1f3,#d9dbe0);border-radius:6px" role="img" aria-label="Three smartphones showing pie and bar chart dashboards"></div>

  <!-- testimonials -->
  <section class="abs quotes"></section>
  <h2 class="abs center h2" style="top:897px">What People Say</h2>
  <span class="abs chev" style="left:17px;top:979px">‹</span>
  <span class="abs chev" style="left:421px;top:979px">›</span>
  <div class="abs quote" style="left:37px;top:932px">
    <div class="quote-mark">“</div>
    <p class="quote-text" style="margin-left:15px">Excepteur sint occaecat cupidatat non proident, sunt in culpa qui officia deserunt mollit anim id est laborum.</p>
  </div>
  <div class="abs quote" style="left:221px;top:932px">
    <div class="quote-mark">“</div>
    <p class="quote-text" style="margin-left:16px">Sed ut perspiciatis unde omnis iste natus error sit voluptatem accusantium doloremque laudantium, totam rem aperiam.</p>
  </div>
  <div class="abs quote-rule" style="left:52px;top:1014px;width:156px"></div>
  <div class="abs quote-rule" style="left:237px;top:1014px;width:157px"></div>
  <div class="abs" style="left:52px;top:1021px"><div class="quote-name">JOHNATHAN SMITH</div><div class="quote-role">Vice President Information Technology, Company Name</div></div>
  <div class="abs" style="left:237px;top:1021px"><div class="quote-name">MARY SMYTH</div><div class="quote-role">Director and Co-Founder, Company Name</div></div>

  <!-- demo -->
  <section class="abs demo" role="img" aria-label="Dimmed photo of two people shaking hands over a laptop"></section>
  <h2 class="abs center" style="top:1121px;font-size:20px;font-weight:400;color:var(--white)">Demo Our Software</h2>
  <svg class="abs" style="left:194px;top:1169px" width="56" height="56" viewBox="0 0 56 56"><circle cx="28" cy="28" r="28" fill="var(--pink-deep)"/><path d="M22 19l15 9-15 9z" fill="#fff"/></svg>
  <p class="abs center" style="top:1247px;font-size:9px;line-height:11px;color:#e3e3ea">Duis aute irure dolor in<br>reprehenderit in voluptate velit<br>esse cillum dolore eu fugiat nulla</p>

  <!-- team -->
  <h2 class="abs center" style="top:1381px;font-size:20px;font-weight:400">Meet Our Team</h2>
  <p class="abs center sub" style="top:1406px">Lorem ipsum dolor sit amet, consectetur<br>adipiscing elit, sed do eiusmod tempor</p>
  <span class="abs chev" style="left:14px;top:1519px">‹</span>
  <span class="abs chev" style="left:419px;top:1519px">›</span>
  <div class="abs member" style="left:39px;top:1465px">
    <span class="avatar" role="img" aria-label="Portrait of team member"></span>
    <p class="m-text">Lorem ipsum dolor sit amet,<br>consectetur adipiscing elit,<br>sed do eiusmod tempor<br>incididunt ut labore et dolor.</p>
    <p class="m-name">MARIO SMITH</p><p class="m-role">Lead Developer at<br>Company Name</p>
  </div>
  <div class="abs member" style="left:162px;top:1465px">
    <span class="avatar" role="img" aria-label="Portrait of team member"></span>
    <p class="m-text">Ut enim ad minim veniam,<br>quis nostrud exercitation<br>ullamco laboris nisi ut.</p>
    <p class="m-name" style="margin-top:14px">JOHN SMYTH</p><p class="m-role">Director atCompany<br>Name</p>
  </div>
  <div class="abs member card" style="left:286px;top:1453px;height:149px;padding-top:15px">
    <span class="avatar" role="img" aria-label="Portrait of team member"></span>
    <p class="m-text">Aliquip ex ea commodo<br>consequat. Duis aute irure dolor<br>in reprehenderit in voluptate<br>velit esse cillum dolore eu fugiat</p>
    <p class="m-name" style="margin-top:15px">MARVIN SMYTH</p><p class="m-role">Buyer at<br>Company Name</p>
  </div>
  <div class="abs btn" style="left:188px;top:1632px;width:59px;height:16px;background:var(--pink-deep)">Learn more</div>

  <!-- join -->
  <section class="abs join"></section>
  <h2 class="abs center" style="top:1746px;font-size:20px;font-weight:400;color:var(--white)">Join Our Program</h2>
  <p class="abs center" style="top:1775px;font-size:9px;line-height:10px;color:#e6e6e6">Sed do eiusmod tempor incididunt<br>ut labore et dolore magna aliqua.</p>
  <div class="abs email">Email</div>
  <div class="abs btn" style="left:273px;top:1820px;width:59px;height:15px">Subscribe</div>

  <!-- footer -->
  <footer class="abs footer">
    <span class="abs" style="left:62px;top:17px;width:20px;height:20px;border-radius:50%;background:var(--pink)"></span>
    <span class="abs" style="left:88px;top:23px;font-size:8px;font-weight:500">TENDWELL</span>
    <p class="abs" style="left:135px;top:16px">123 Street,<br>Anytown, USA 12345</p>
    <p class="abs" style="left:135px;top:33px">hello@website.com</p>
    <p class="abs" style="left:269px;top:33px">© 2020 Tendwell. All rights reserved</p>
  </footer>

</div>
</div>
</body>
</html>
```